Company brochure for our unique consulting business

We are a small consulting business offering a unique set of services to our clients.. In simple terms we are a business improvement consultancy helping our clients get the best out of their businesses. We work with clients across multiple sectors and deliver a variety of services. We want to put together a brochure to cover these main themes:1. Who we are2. What we do3. The type of people we employ4. The sectors we work inWhile the brochure needs to have a certain corporate feel to it, we don't want it to be "boring" or "stiff". We would like it to have a slightly "friendly" or "informal" feel to it, to reflect the type of organisation we are.We have a company website http://tollandvergeadvisory.com , however we do not want to directly replicate the content or feel as we recognise it needs updating.We would like the brochure to be A4 portrait format. We anticipate requiring 12 sides (including covers) but we are happy to be guided on this based on the content we have provided.The attached ppt file gives the detail of the content to be included and also shows the proposed pagination. For the front cover we would like to try 2 versions, one with the TVA logo and one with the Tolland Verge Advisory logo (a file of both is attached)One of the most important pages will be the "Our Services" page. We would like this to cover the centre fold. In the ppt file we have shown an example layout, but this is where we need most help - we are clearly not graphic designers! This page will be the most used page in sales meetings etc.Also attached is the following:1. file for our TollandVerge Advisory company logo.2. File for our TVA company logo3. Files for Derek's signatures (for under photos) - Owen's to follow4. Photo of Derek & Owen (person in purple shirt to be cropped out)Thank you and really excited to see what everyone comes back with.Derek & Owen

Target Market(s)

Very broad - Manufacturing, Healthcare, Hospitality

Industry/Entity Type

Management Consulting

Font styles to use
Other font styles liked:
• We use Swiss721, but happy to be guided by designer

Colors
3276b5
85abd2
0355a3
333333
5c5c5c
9d9d9d
d9d9d9

Requirements
Must have
• Corporate feel
Nice to have
• Slightly friendly feel
• Our standard "blue" is (CORRECTION) - R55 G96 B146 #376092 and our standard grey is R197 G178, B179 - #B3B2B2, which we would like to keep, but other colours we are happy to be guided on. Brand guidelines attached.

```html
<!DOCTYPE html>
<html lang="en">
<head>
<meta charset="utf-8">
<title>TVA Brochure – Cover and Our Services Spread</title>
<link rel="stylesheet" href="https://fonts.googleapis.com/css2?family=Arimo:wght@400;700&family=Roboto+Condensed:wght@300;400&display=swap">
<style>
  :root {
    --brand-blue: #376092;
    --brand-blue-bright: #3276b5;
    --brand-blue-light: #85abd2;
    --brand-navy: #0f2457;
    --brand-deep: #0355a3;
    --ink: #333333;
    --ink-soft: #5c5c5c;
    --grey-mid: #9d9d9d;
    --grey-light: #d9d9d9;
    --paper: #eeeeee;
    --stage: #f4f4f2;
  }
  * { box-sizing: border-box; margin: 0; padding: 0; }
  html, body { width: 1200px; height: 900px; overflow: hidden; }
  body {
    background: var(--stage);
    font-family: "Arimo", Arial, sans-serif;
    position: relative;
  }
  .cover {
    position: absolute; left: 700px; top: 20px;
    width: 460px; height: 280px;
    box-shadow: 0 6px 18px rgba(0,0,0,.18);
  }
  .spread {
    position: absolute; left: 20px; top: 320px;
    width: 1160px; height: 560px;
    box-shadow: 0 6px 18px rgba(0,0,0,.18);
  }
  svg { display: block; }
  .cover-brand { font-family: "Arimo", Arial, sans-serif; font-weight: 700; fill: #111; }
  .cover-tagline { font-family: "Roboto Condensed", "Arial Narrow", sans-serif; font-weight: 300; fill: #fff; }
  .services-title { font-weight: 700; fill: #fff; }
  .services-intro { fill: #fff; }
  .venn-title { font-weight: 700; font-size: 11px; }
  .venn-sub { font-size: 9px; }
  .bubble-label { font-size: 7px; fill: var(--ink); text-anchor: middle; }
  .link-green { stroke: #4b9a3a; stroke-width: 1; }
  .link-yellow { stroke: #c59a24; stroke-width: 1; }
  .link-red { stroke: #a3272b; stroke-width: 1; }
  .intro-copy { font-size: 11.5px; fill: var(--ink); text-anchor: end; }
</style>
</head>
<body>

<section class="cover" aria-label="Front cover">
  <svg width="460" height="280" viewBox="0 0 460 280">
    <defs>
      <linearGradient id="cover-photo-tone" x1="0" y1="0" x2="1" y2="1">
        <stop offset="0" stop-color="#1d4f9a"/>
        <stop offset=".55" stop-color="#6f9fd6"/>
        <stop offset="1" stop-color="#c9dcf0"/>
      </linearGradient>
    </defs>
    <rect class="cover-paper" width="460" height="280" fill="#e6e7e9"/>
    <polygon class="cover-top-band" points="0,0 460,0 460,8 0,14" fill="var(--brand-navy)"/>
    <polygon class="cover-photo" role="img" aria-label="Photo of a businessman with briefcase facing a night city skyline under a connected globe"
      points="300,40 460,34 460,150 330,280 200,280" fill="url(#cover-photo-tone)"/>
    <polygon class="cover-accent" points="200,280 300,40 312,40 214,280" fill="var(--brand-deep)"/>
    <text class="cover-brand" x="22" y="80" font-size="56">tva</text>
    <polygon class="cover-tagline-box" points="8,100 240,100 180,250 8,250" fill="var(--brand-blue)"/>
    <text class="cover-tagline" x="22" y="142" font-size="26">
      <tspan x="22">Better</tspan><tspan x="22" dy="28">People</tspan>
      <tspan x="22" dy="44">Better</tspan><tspan x="22" dy="28">Business</tspan>
    </text>
  </svg>
</section>

<section class="spread" aria-label="Our Services centre spread">
  <svg width="1160" height="560" viewBox="0 0 1160 560">
    <defs>
      <linearGradient id="spread-paper" x1="0" y1="0" x2="1" y2="1">
        <stop offset="0" stop-color="#c4c4c4"/>
        <stop offset="1" stop-color="#a9a9a9"/>
      </linearGradient>
      <radialGradient id="bubble-green" cx=".4" cy=".35" r=".7">
        <stop offset="0" stop-color="#8fd47a"/><stop offset="1" stop-color="#3d8f2c"/>
      </radialGradient>
      <radialGradient id="bubble-yellow" cx=".4" cy=".35" r=".7">
        <stop offset="0" stop-color="#f2cc6a"/><stop offset="1" stop-color="#c18d1c"/>
      </radialGradient>
      <radialGradient id="bubble-red" cx=".4" cy=".35" r=".7">
        <stop offset="0" stop-color="#ee8a86"/><stop offset="1" stop-color="#b8383a"/>
      </radialGradient>
      <clipPath id="clip-pm"><circle cx="540" cy="260" r="95"/></clipPath>
      <clipPath id="clip-bi"><circle cx="640" cy="310" r="95"/></clipPath>
    </defs>

    <rect class="spread-paper" width="1160" height="560" fill="url(#spread-paper)"/>
    <polygon class="spread-panel-light" points="0,300 330,190 420,200 0,380" fill="#d2d2d2"/>
    <line class="spread-fold" x1="580" y1="0" x2="580" y2="560" stroke="#9a9a9a" stroke-width="1"/>

    <!-- Our Services header -->
    <polygon class="services-header" points="0,0 560,0 330,190 0,300" fill="var(--brand-blue)"/>
    <text class="services-title" x="28" y="52" font-size="30">Our Services</text>
    <text class="services-intro" x="28" y="82" font-size="13">
      <tspan x="28">Three blended offerings, tailored to your organisation.</tspan>
      <tspan x="28" dy="26">A blended approach, tailored to each</tspan>
      <tspan x="28" dy="17">organisation, across 3 core offerings</tspan>
    </text>

    <!-- Right page intro panel -->
    <polygon class="intro-band" points="920,255 1160,222 1160,560 840,560" fill="var(--brand-blue)"/>
    <polygon class="intro-panel" points="965,262 1160,245 1160,560 888,560" fill="#f1f1f1"/>
    <text class="intro-copy">
      <tspan x="1145" y="292">We recognize every</tspan>
      <tspan x="1145" dy="16">organisation we work with</tspan>
      <tspan x="1145" dy="16">is different; the products or</tspan>
      <tspan x="1145" dy="16">services provided, the culture and</tspan>
      <tspan x="1145" dy="16">the readiness for change but most</tspan>
      <tspan x="1145" dy="16">importantly the 'wants and needs' are</tspan>
      <tspan x="1145" dy="16">always unique. The skills, knowledge</tspan>
      <tspan x="1145" dy="16">and experience across our team means</tspan>
      <tspan x="1145" dy="16">we are able to offer an extensive range</tspan>
      <tspan x="1145" dy="16">of services which are tailored to meet your</tspan>
      <tspan x="1145" dy="16">specific needs.</tspan>
    </text>

    <!-- Connectors -->
    <g class="links-green">
      <line class="link-green" x1="540" y1="260" x2="90" y2="330"/>
      <line class="link-green" x1="540" y1="260" x2="160" y2="300"/>
      <line class="link-green" x1="540" y1="260" x2="230" y2="275"/>
      <line class="link-green" x1="540" y1="260" x2="300" y2="255"/>
      <line class="link-green" x1="540" y1="260" x2="380" y2="200"/>
      <line class="link-green" x1="540" y1="260" x2="455" y2="178"/>
      <line class="link-green" x1="540" y1="260" x2="150" y2="400"/>
      <line class="link-green" x1="540" y1="260" x2="250" y2="400"/>
    </g>
    <g class="links-yellow">
      <line class="link-yellow" x1="550" y1="365" x2="120" y2="455"/>
      <line class="link-yellow" x1="550" y1="365" x2="190" y2="505"/>
      <line class="link-yellow" x1="550" y1="365" x2="290" y2="530"/>
      <line class="link-yellow" x1="550" y1="365" x2="400" y2="532"/>
      <line class="link-yellow" x1="550" y1="365" x2="500" y2="532"/>
      <line class="link-yellow" x1="550" y1="365" x2="585" y2="505"/>
    </g>
    <g class="links-red">
      <line class="link-red" x1="640" y1="310" x2="690" y2="125"/>
      <line class="link-red" x1="640" y1="310" x2="765" y2="140"/>
      <line class="link-red" x1="640" y1="310" x2="835" y2="170"/>
      <line class="link-red" x1="640" y1="310" x2="870" y2="235"/>
      <line class="link-red" x1="640" y1="310" x2="760" y2="265"/>
      <line class="link-red" x1="640" y1="310" x2="860" y2="300"/>
      <line class="link-red" x1="640" y1="310" x2="770" y2="330"/>
      <line class="link-red" x1="640" y1="310" x2="850" y2="370"/>
      <line class="link-red" x1="640" y1="310" x2="770" y2="400"/>
      <line class="link-red" x1="640" y1="310" x2="830" y2="450"/>
      <line class="link-red" x1="640" y1="310" x2="740" y2="470"/>
      <line class="link-red" x1="640" y1="310" x2="700" y2="528"/>
      <line class="link-red" x1="640" y1="310" x2="665" y2="478"/>
      <line class="link-red" x1="640" y1="310" x2="700" y2="420"/>
    </g>

    <!-- Venn of three core offerings -->
    <g class="venn">
      <circle class="venn-pm" cx="540" cy="260" r="95" fill="#5d9ad6"/>
      <circle class="venn-or" cx="550" cy="365" r="95" fill="#2f7ac2"/>
      <circle class="venn-bi" cx="640" cy="310" r="95" fill="var(--brand-navy)"/>
      <circle class="venn-pm-bi" cx="640" cy="310" r="95" fill="#b03030" clip-path="url(#clip-pm)"/>
      <circle class="venn-pm-or" cx="550" cy="365" r="95" fill="#4c9a3a" clip-path="url(#clip-pm)"/>
      <circle class="venn-bi-or" cx="550" cy="365" r="95" fill="#d6a53a" clip-path="url(#clip-bi)"/>
      <g clip-path="url(#clip-pm)">
        <circle class="venn-core" cx="550" cy="365" r="95" fill="#222" clip-path="url(#clip-bi)"/>
      </g>
      <text class="venn-title" x="520" y="200" fill="var(--brand-navy)" text-anchor="middle">
        <tspan x="520">Programme</tspan><tspan x="520" dy="13">Management</tspan>
      </text>
      <text class="venn-sub" x="520" y="232" fill="var(--brand-navy)" text-anchor="middle">
        <tspan x="520">Managing programmes</tspan><tspan x="520" dy="11">through to successful</tspan><tspan x="520" dy="11">delivery</tspan>
      </text>
      <text class="venn-title" x="690" y="290" fill="#fff" text-anchor="middle">
        <tspan x="690">Business</tspan><tspan x="690" dy="13">Improvement</tspan>
      </text>
      <text class="venn-sub" x="690" y="322" fill="#fff" text-anchor="middle">
        <tspan x="690">Helping your</tspan><tspan x="690" dy="11">organisation</tspan><tspan x="690" dy="11">perform at it's best</tspan>
      </text>
      <text class="venn-title" x="520" y="402" fill="var(--brand-navy)" text-anchor="middle">
        <tspan x="520">Organisational</tspan><tspan x="520" dy="13">Readiness</tspan>
      </text>
      <text class="venn-sub" x="520" y="432" fill="var(--brand-navy)" text-anchor="middle">
        <tspan x="520">Getting your business</tspan><tspan x="520" dy="11">ready for it's future</tspan>
      </text>
    </g>

    <!-- Programme Management bubbles -->
    <g class="bubbles-green">
      <g transform="translate(90,330)"><ellipse rx="32" ry="19" fill="url(#bubble-green)"/><text class="bubble-label" y="-1"><tspan x="0">Major</tspan><tspan x="0" dy="8">Events</tspan></text></g>
      <g transform="translate(160,300)"><ellipse rx="32" ry="19" fill="url(#bubble-green)"/><text class="bubble-label" y="-1"><tspan x="0">New</tspan><tspan x="0" dy="8">Employees</tspan></text></g>
      <g transform="translate(230,275)"><ellipse rx="32" ry="19" fill="url(#bubble-green)"/><text class="bubble-label" y="-1"><tspan x="0">Facility</tspan><tspan x="0" dy="8">Relocation</tspan></text></g>
      <g transform="translate(300,255)"><ellipse rx="32" ry="19" fill="url(#bubble-green)"/><text class="bubble-label" y="-1"><tspan x="0">Customer</tspan><tspan x="0" dy="8">Acquisition</tspan></text></g>
      <g transform="translate(380,200)"><ellipse rx="32" ry="19" fill="url(#bubble-green)"/><text class="bubble-label" y="-1"><tspan x="0">IT Systems</tspan><tspan x="0" dy="8">Introduction</tspan></text></g>
      <g transform="translate(455,178)"><ellipse rx="32" ry="19" fill="url(#bubble-green)"/><text class="bubble-label" y="-1"><tspan x="0">New Product</tspan><tspan x="0" dy="8">Launch</tspan></text></g>
      <g transform="translate(150,400)"><ellipse rx="28" ry="19" fill="url(#bubble-green)"/><text class="bubble-label" y="3">ISO</text></g>
      <g transform="translate(250,400)"><ellipse rx="28" ry="19" fill="url(#bubble-green)"/><text class="bubble-label" y="3">Cost</text></g>
    </g>

    <!-- Organisational Readiness bubbles -->
    <g class="bubbles-yellow">
      <g transform="translate(120,455)"><ellipse rx="30" ry="19" fill="url(#bubble-yellow)"/><text class="bubble-label" y="3">Sale</text></g>
      <g transform="translate(190,505)"><ellipse rx="32" ry="19" fill="url(#bubble-yellow)"/><text class="bubble-label" y="3">Acquisition</text></g>
      <g transform="translate(290,530)"><ellipse rx="32" ry="19" fill="url(#bubble-yellow)"/><text class="bubble-label" y="3">Separation</text></g>
      <g transform="translate(400,532)"><ellipse rx="30" ry="19" fill="url(#bubble-yellow)"/><text class="bubble-label" y="3">Merger</text></g>
      <g transform="translate(500,532)"><ellipse rx="30" ry="19" fill="url(#bubble-yellow)"/><text class="bubble-label" y="3">Growth</text></g>
      <g transform="translate(585,505)"><ellipse rx="32" ry="19" fill="url(#bubble-yellow)"/><text class="bubble-label" y="3">Optimisation</text></g>
    </g>

    <!-- Business Improvement bubbles -->
    <g class="bubbles-red">
      <g transform="translate(690,125)"><ellipse rx="32" ry="19" fill="url(#bubble-red)"/><text class="bubble-label" y="-1"><tspan x="0">Business</tspan><tspan x="0" dy="8">Development</tspan></text></g>
      <g transform="translate(765,140)"><ellipse rx="32" ry="19" fill="url(#bubble-red)"/><text class="bubble-label" y="-1"><tspan x="0">Customer</tspan><tspan x="0" dy="8">Service</tspan></text></g>
      <g transform="translate(835,170)"><ellipse rx="32" ry="19" fill="url(#bubble-red)"/><text class="bubble-label" y="-1"><tspan x="0">Quality</tspan><tspan x="0" dy="8">Systems</tspan></text></g>
      <g transform="translate(870,235)"><ellipse rx="33" ry="19" fill="url(#bubble-red)"/><text class="bubble-label" y="-4"><tspan x="0">Leadership</tspan><tspan x="0" dy="8">coaching &amp;</tspan><tspan x="0" dy="8">mentoring</tspan></text></g>
      <g transform="translate(760,265)"><ellipse rx="32" ry="19" fill="url(#bubble-red)"/><text class="bubble-label" y="-1"><tspan x="0">Process</tspan><tspan x="0" dy="8">design</tspan></text></g>
      <g transform="translate(860,300)"><ellipse rx="32" ry="19" fill="url(#bubble-red)"/><text class="bubble-label" y="-1"><tspan x="0">Facility</tspan><tspan x="0" dy="8">Design</tspan></text></g>
      <g transform="translate(770,330)"><ellipse rx="33" ry="19" fill="url(#bubble-red)"/><text class="bubble-label" y="-1"><tspan x="0">New Product</tspan><tspan x="0" dy="8">Introduction</tspan></text></g>
      <g transform="translate(850,370)"><ellipse rx="32" ry="19" fill="url(#bubble-red)"/><text class="bubble-label" y="3">Programme</text></g>
      <g transform="translate(770,400)"><ellipse rx="32" ry="19" fill="url(#bubble-red)"/><text class="bubble-label" y="-4"><tspan x="0">Logistics</tspan><tspan x="0" dy="8">and</tspan><tspan x="0" dy="8">planning</tspan></text></g>
      <g transform="translate(830,450)"><ellipse rx="30" ry="19" fill="url(#bubble-red)"/><text class="bubble-label" y="3">Personal</text></g>
      <g transform="translate(740,470)"><ellipse rx="33" ry="19" fill="url(#bubble-red)"/><text class="bubble-label" y="-4"><tspan x="0">Senior</tspan><tspan x="0" dy="8">leadership</tspan><tspan x="0" dy="8">development</tspan></text></g>
      <g transform="translate(700,528)"><ellipse rx="30" ry="19" fill="url(#bubble-red)"/><text class="bubble-label" y="3">Strategy</text></g>
      <g transform="translate(665,478)"><ellipse rx="33" ry="19" fill="url(#bubble-red)"/><text class="bubble-label" y="-1"><tspan x="0">Organisational</tspan><tspan x="0" dy="8">design</tspan></text></g>
      <g transform="translate(700,420)"><ellipse rx="32" ry="19" fill="url(#bubble-red)"/><text class="bubble-label" y="-1"><tspan x="0">Quality</tspan><tspan x="0" dy="8">Improvement</tspan></text></g>
    </g>
  </svg>
</section>

</body>
</html>
```